RVT studios

rvt studios is an interior design firm in omaha, NE. Offering complete residential/commercial design. Exterior, int finishes, cabinets, furniture, window covering. Have been in business for 25 yrs. Lived in and/or completed work in LA, NYC, PHX, MIami, London, Canada, Mexico. We would like to see a marketing flyer with clean, architectural design. Modern .Flyer will be on display at open houses & mailed to perspective clients. Dont want a lot of color. Prefer whites/black, greys or brown. Maybe small accent of blue like logo. Block architectural lettering. do not need to use all photos. but use at least one from each of the three projects. thanks for you time

please change/add on any and all submissions the following add: Dana Whitcombe, Principal (in info section not on logo) change: Info@rvtstudios.com, not dana @rvtstudios.com add: back design, would like to use as many photos as possible thanks you

```html
<!DOCTYPE html>
<html lang="en">
<head>
<meta charset="utf-8">
<title>RVT studios flyer</title>
<link rel="stylesheet" href="https://fonts.googleapis.com/css2?family=Open+Sans:wght@400;600;700&display=swap">
<style>
  :root {
    --accent: #3f7fb5;
    --frame-line: #4a4643;
    --ink: #333333;
    --muted: #4a4a4a;
    --paper-top: #f4f4f4;
    --paper-bottom: #dcdcdc;
    --photo-border: #ffffff;
    --footer: #1d1d1d;
    --footer-text: #ffffff;
  }
  * { box-sizing: border-box; margin: 0; padding: 0; }
  html, body { width: 876px; height: 1200px; overflow: hidden; }
  body { font-family: "Open Sans", Arial, sans-serif; }
  .flyer {
    position: relative;
    width: 876px; height: 1200px;
    background: linear-gradient(160deg, var(--paper-top) 0%, #ececec 55%, var(--paper-bottom) 100%);
    overflow: hidden;
  }
  .accent-frame {
    position: absolute;
    left: 75px; top: 70px;
    width: 690px; height: 640px;
    border: 14px solid var(--frame-line);
    transform: rotate(8deg);
  }
  .hero-photo {
    position: absolute;
    left: 70px; top: 80px;
    width: 670px; height: 620px;
    background: var(--photo-border);
    padding: 14px;
    transform: rotate(-7deg);
    box-shadow: 0 6px 18px rgba(0,0,0,0.25);
  }
  .hero-photo .fill {
    width: 100%; height: 100%;
    background: linear-gradient(180deg, #d9d2c4 0%, #b89c78 30%, #6b4b30 58%, #2e241d 80%, #5a3c24 100%);
  }
  .contact-block {
    position: absolute;
    right: 70px; top: 760px;
    text-align: right;
  }
  .call-label {
    font-weight: 700;
    font-size: 24px;
    color: var(--accent);
  }
  .principal {
    font-weight: 600;
    font-size: 22px;
    color: var(--ink);
    margin-top: 2px;
  }
  .phone {
    display: flex; align-items: center; justify-content: flex-end;
    gap: 10px;
    font-size: 38px;
    color: var(--ink);
    margin-top: 2px;
  }
  .phone svg { width: 34px; height: 34px; }
  .intro {
    position: absolute;
    right: 70px; top: 905px;
    width: 760px;
    text-align: right;
    font-size: 29px;
    line-height: 1.3;
    color: var(--muted);
  }
  .project-photos {
    position: absolute;
    left: 60px; top: 1005px;
    display: flex; gap: 20px;
  }
  .project-photo {
    width: 160px; height: 100px;
    background: var(--photo-border);
    padding: 6px;
    box-shadow: 0 3px 10px rgba(0,0,0,0.2);
  }
  .project-photo .fill { width: 100%; height: 100%; }
  .project-photo.kitchen .fill { background: linear-gradient(180deg, #e6e1d8 0%, #a9a39a 50%, #4f4a45 100%); }
  .project-photo.living .fill { background: linear-gradient(180deg, #d8cbb8 0%, #8f7558 55%, #3d2c20 100%); }
  .brand {
    position: absolute;
    right: 100px; top: 1020px;
    display: flex; align-items: center; gap: 16px;
  }
  .brand-square { width: 70px; height: 70px; background: var(--accent); }
  .brand-name {
    font-weight: 600;
    font-size: 46px;
    color: var(--ink);
  }
  .footer {
    position: absolute;
    left: 0; bottom: 0;
    width: 100%; height: 72px;
    background: var(--footer);
    color: var(--footer-text);
    display: flex; align-items: center; justify-content: space-between;
    padding: 0 70px 0 55px;
    font-size: 23px;
  }
  .footer-item { display: flex; align-items: center; gap: 12px; }
  .footer-item svg { width: 28px; height: 28px; }
</style>
</head>
<body>
  <main class="flyer">
    <div class="accent-frame"></div>
    <div class="hero-photo">
      <div class="fill" role="img" aria-label="Photo of a finished home bar with stone wall, dark granite counter, bar stools and lit shelving"></div>
    </div>

    <section class="contact-block">
      <p class="call-label">Call Us Now</p>
      <p class="principal">Dana Whitcombe, Principal</p>
      <p class="phone">
        <svg viewBox="0 0 24 24" aria-hidden="true">
          <circle cx="12" cy="12" r="10.5" fill="none" stroke="#333333" stroke-width="1.8"/>
          <path d="M8.3 6.8c.4-.4 1-.4 1.3 0l1.2 1.6c.3.4.3.9-.1 1.2l-.7.6c.6 1.3 1.6 2.3 2.9 2.9l.6-.7c.3-.4.8-.4 1.2-.1l1.6 1.2c.4.3.4.9 0 1.3l-.8.8c-.6.6-1.5.7-2.3.3-2.4-1.1-4.3-3-5.4-5.4-.4-.8-.3-1.7.3-2.3z" fill="#333333"/>
        </svg>
        402 555 0148
      </p>
    </section>

    <p class="intro">RVT studios has offerdcomplete<br>design services for resedential and commercial</p>

    <div class="project-photos">
      <div class="project-photo kitchen"><div class="fill" role="img" aria-label="Photo of a finished kitchen project with grey cabinets"></div></div>
      <div class="project-photo living"><div class="fill" role="img" aria-label="Photo of a finished living room project with warm wood finishes"></div></div>
    </div>

    <div class="brand">
      <span class="brand-square"></span>
      <span class="brand-name">RVT studios</span>
    </div>

    <footer class="footer">
      <span class="footer-item">
        <svg viewBox="0 0 24 24" aria-hidden="true" fill="none" stroke="#ffffff" stroke-width="1.6">
          <circle cx="12" cy="12" r="9.5"/>
          <ellipse cx="12" cy="12" rx="4" ry="9.5"/>
          <path d="M2.5 12h19M4 7h16M4 17h16"/>
        </svg>
        www.rvtstudios.com
      </span>
      <span class="footer-item">
        <svg viewBox="0 0 24 24" aria-hidden="true">
          <rect x="2" y="5" width="20" height="14" rx="1.5" fill="#ffffff"/>
          <path d="M2.5 6l9.5 7 9.5-7" fill="none" stroke="#1d1d1d" stroke-width="1.6"/>
        </svg>
        Info@rvtstudios.com
      </span>
    </footer>
  </main>
</body>
</html>
```